Outdoor sign for Brindle Auto Restoration

I need a horizontal 4'x 8' outdoor roadside sign for my classic auto restoration business. I have uploaded colors and our logo. Needs the Brindle name, a prominent Classic AUTO RESTORATION, phone number and website. We rebuild and restore vintage cars, trucks and 4x4s. I'd like something clean but possibly retro. Classic Auto Restoration is more important than the Brindle name. It needs to be visible and readable from the street. NO CLIP ART

Target Market(s)

Customers who need their vintage care restored or upgraded. Men and women ages 25-75

Industry/Entity Type

Automotive

Colors
FFC000
F8CF3A
FAE287
FDF2CF
FEFAEE

Requirements
Must have
• Legible. Bright. Readable as a backlit 4' x 8' large horizontal sign (roughly 120cm X 240cm)
Nice to have
• Use of the Brindle logo/type, Complete or Classic before prominent AUTO RESTORATION
Should not have
• Clip art of old cars or icons. And we don't want the Brindle Logo from the website because it wont be legible from the road. I have included the Illustrator file for Brindle text in the uploads

```html
<!DOCTYPE html>
<html lang="en">
<head>
<meta charset="utf-8">
<title>Brindle Auto Restoration – Roadside Sign</title>
<link rel="stylesheet" href="https://fonts.googleapis.com/css2?family=Anton&family=Graduate&family=Oswald:wght@700&display=swap">
<style>
  :root {
    --backdrop: #f9d78d;
    --sign-dark: #2c2322;
    --sign-gold: #f4af00;
  }
  html, body {
    margin: 0;
    padding: 0;
    width: 1200px;
    height: 728px;
    overflow: hidden;
    background: var(--backdrop);
  }
  .sign-canvas {
    display: block;
    width: 1200px;
    height: 728px;
  }
  .sign-panel { fill: var(--sign-dark); }
  .contact-band { fill: var(--sign-gold); }
  .brand-name {
    font-family: "Anton", "Oswald", sans-serif;
    font-size: 84px;
    fill: var(--sign-gold);
  }
  .headline {
    font-family: "Graduate", "Rockwell", serif;
    font-size: 124px;
    fill: var(--sign-gold);
  }
  .contact {
    font-family: "Oswald", "Roboto Condensed", sans-serif;
    font-weight: 700;
    font-size: 52px;
    fill: var(--sign-dark);
  }
</style>
</head>
<body>
<svg class="sign-canvas" viewBox="0 0 1200 728" xmlns="http://www.w3.org/2000/svg" role="img" aria-label="Brindle Classic Auto Restoration sign">
  <defs>
    <filter id="sign-shadow" x="-5%" y="-5%" width="110%" height="110%">
      <feDropShadow dx="3" dy="3" stdDeviation="2" flood-color="#000" flood-opacity="0.45"/>
    </filter>
  </defs>

  <g class="sign" filter="url(#sign-shadow)">
    <rect class="sign-panel" x="75.5" y="101.8" width="1048.5" height="524.2"/>
    <rect class="contact-band" x="75.5" y="550" width="1048.5" height="76"/>
  </g>

  <text class="brand-name" x="1093" y="198" text-anchor="end" textLength="390" lengthAdjust="spacingAndGlyphs">BRINDLE</text>

  <text class="headline" x="107" y="356.5" textLength="934" lengthAdjust="spacingAndGlyphs">CLASSIC AUTO</text>
  <text class="headline" x="196" y="481.5" textLength="897" lengthAdjust="spacingAndGlyphs">RESTORATION</text>

  <text class="contact phone" x="107" y="608" textLength="226" lengthAdjust="spacingAndGlyphs">501-555-0142</text>
  <text class="contact web" x="1093" y="608" text-anchor="end" textLength="434" lengthAdjust="spacingAndGlyphs">brindle autoworks.com</text>
</svg>
</body>
</html>
```